Guiding Your Revenue Overhaul *

Bold eye-catching design for business non-fiction: I am seeking a bold, and clean design for a book. The book will be 6X9 for both the ebook and in print. I am open to ideas, but found that books like “steady as rain” with contrast are highly desirable for business books.

I am open to color choices.

I would also like a growth orientated graphic in the book - something to show growth, leadership, movement. Not just a plain graphic.

The title:

Guiding Your Revenue Overhaul

The subtitle - I am open to suggestions. Two subtitles I am considering:

A framework for new sales leaders and those who want to keep winning.

A guide for new sales leaders and those who want to keep winning.

The below is an introduction of the book: (Back Jacket)

Sales transformation is a topic that is infrequently written about. For the new sales leader, there are a myriad of books written on coaching, leadership, forecasting, solution selling and sales process but very little is written about how to assess a sales team and build a plan for long-term success.

Through my sales leadership career, whether recently promoted or starting with a new team, I have often asked the question: Where do I start?

In the end, I was disappointed with the answers from currently available books and research, left to figure it out myself - which I did over a decade, with great pain and through many transformations. The inability to answer the question – Where do I start? – is why I wrote this book. To answer that question.

The goal of this book is to help sales leaders answer that question by providing a framework to understand the business, build a plan, and guide the team through the different stages of a sales transformation. A framework to succeed at the fastest pace possible, quarter after quarter.

(End back jacket - the rest is just additional context)

Over the last decade, I have had the privilege of leading teams in North America, Europe, and Asia. I have led turnarounds, growth businesses, and realignments. Each team was different in size, complexity, and culture; and each one offered up new and unique challenges. Each team operated with different market dynamics: one was a commodity; one was a low-cost leader; one was a market innovator. Each transformation helped me learn by taking risks, by failing and by succeeding. At each step, I had many teachers; and as I learned, I made notes. Over time I built a framework that you can leverage as you read and absorb this book. As you lead your team through a sales transformation.

I hope that this book will become for you what The Copper Lantern is for me: a favorite on your bookshelf; underlined, highlighted, dog-eared, and an ongoing reference.

Sales leadership is a journey. It is never linear, and it is always changing. At different times, different parts of this book will apply, while others will not, but hopefully, you will find it a useful and long-lasting reference.

Target Market(s)

Business readers. Sales leaders.

Requirements
Must have
• Modern, clear, eye catching colours. Clean. Graphics that indicate growth, leadership, strength.
• Please ensure the design has the full cover and back jacket design. Please use the introduction of the book as the back jacket text.

```html
<!DOCTYPE html>
<html lang="en">
<head>
<meta charset="utf-8">
<title>Guiding Your Revenue Overhaul – Cover Spread</title>
<link href="https://fonts.googleapis.com/css2?family=Ubuntu:wght@400;500;700&display=swap" rel="stylesheet">
<style>
  :root {
    --backdrop: #efeff1;
    --cover-red: #e92227;
    --ink-white: #ffffff;
    --ink-dark: #2b2b2b;
    --figure-dark: #262626;
  }
  * { margin: 0; padding: 0; box-sizing: border-box; }
  html, body {
    width: 1200px; height: 1200px; overflow: hidden;
    background: var(--backdrop);
    font-family: "Ubuntu", sans-serif;
  }
  .canvas { position: relative; width: 1200px; height: 1200px; }
  .spread {
    position: absolute; left: 54px; top: 223px;
    width: 1094px; height: 753px;
    background: var(--cover-red);
  }

  /* Back jacket */
  .back-author {
    position: absolute; left: 0; width: 534px; top: 62px;
    text-align: center; font-weight: 500; font-size: 27px;
    color: var(--ink-dark); letter-spacing: 0.3px;
  }
  .back-title {
    position: absolute; left: 0; width: 534px; top: 108px;
    text-align: center; font-weight: 700; font-size: 36px;
    line-height: 46px; color: var(--ink-white);
  }
  .back-copy {
    position: absolute; left: 30px; width: 441px; top: 243px;
    color: var(--ink-dark); font-size: 16px; line-height: 17.3px;
    text-align: justify; hyphens: auto;
  }
  .back-copy p { margin-bottom: 16px; }

  /* Spine */
  .spine {
    position: absolute; left: 534px; width: 40px; top: 20px; height: 716px;
    writing-mode: vertical-rl;
    display: flex; justify-content: space-between; align-items: center;
    color: var(--ink-white); font-size: 19px; font-weight: 400;
    letter-spacing: 0.5px;
  }

  /* Front cover */
  .front-title { color: var(--ink-white); font-weight: 500; }
  .title-line-1 {
    position: absolute; left: 634px; width: 416px; top: 40px;
    text-align: center; font-size: 74px; line-height: 80px;
  }
  .title-rule {
    position: absolute; top: 156px; height: 6px; background: var(--ink-white);
  }
  .title-rule.left { left: 654px; width: 126px; }
  .title-rule.right { left: 905px; width: 129px; }
  .title-line-2 {
    position: absolute; left: 780px; width: 125px; top: 130px;
    text-align: center; font-size: 44px; line-height: 56px;
  }
  .title-line-3 {
    position: absolute; left: 634px; width: 416px; top: 172px;
    text-align: center; font-size: 80px; line-height: 96px; font-weight: 700;
  }
  .title-line-4 {
    position: absolute; left: 634px; width: 416px; top: 272px;
    text-align: center; font-size: 40px; line-height: 46px;
  }
  .subtitle {
    position: absolute; left: 632px; width: 220px; top: 358px;
    text-align: center; color: var(--ink-dark);
    font-size: 19px; line-height: 24px; font-weight: 500;
  }
  .growth-chart { position: absolute; left: 0; top: 0; }
  .figure-slot {
    position: absolute; left: 884px; top: 372px; width: 134px; height: 318px;
    border-radius: 60px 60px 20px 20px;
    background: linear-gradient(180deg, #3a3a3a 0%, var(--figure-dark) 100%);
    opacity: 0.9;
  }
  .front-author {
    position: absolute; left: 634px; width: 416px; top: 703px;
    text-align: center; font-weight: 700; font-size: 27px;
    color: var(--ink-dark); letter-spacing: 0.3px;
  }
</style>
</head>
<body>
<div class="canvas">
  <div class="spread">

    <section class="back-jacket">
      <div class="back-author">DANIEL OSTRANDER</div>
      <h2 class="back-title">GUIDING YOUR<br>REVENUE OVERHAUL</h2>
      <div class="back-copy">
        <p>Sales transformation is a topic that is infrequently written about. For the new sales leader, there are a myriad of books written on coaching, leadership, forecasting, solution selling and sales process but very little is written about how to assess a sales team and build a plan for long-term success.</p>
        <p>Through my sales leadership career, whether recently promoted or starting with a new team, I have often asked the question: Where do I start?</p>
        <p>In the end, I was disappointed with the answers from currently available books and research, left to figure it out myself - which I did over a decade, with great pain and through many transformations. The inability to answer the question – Where do I start? – is why I wrote this book. To answer that question.</p>
        <p>The goal of this book is to help sales leaders answer that question by providing a framework to understand the business, build a plan, and guide the team through the different stages of a sales transformation. A framework to succeed at the fastest pace possible, quarter after quarter.</p>
      </div>
    </section>

    <div class="spine">
      <span>GUIDING</span><span>YOUR</span><span>REVENUE</span><span>OVERHAUL</span><span>DANIEL</span><span>OSTRANDER</span>
    </div>

    <section class="front-cover">
      <div class="front-title">
        <div class="title-line-1">GUIDING</div>
        <div class="title-rule left"></div>
        <div class="title-line-2">YOUR</div>
        <div class="title-rule right"></div>
        <div class="title-line-3">REVENUE</div>
        <div class="title-line-4">OVERHAUL</div>
      </div>
      <div class="subtitle">A FRAMEWORK<br>FOR NEW SALES<br>LEADERS AND<br>THOSE WHO WANT<br>TO KEEP WINNING</div>

      <svg class="growth-chart" width="1094" height="753" viewBox="0 0 1094 753" aria-hidden="true">
        <polyline points="606,577 656,532 692,570 738,497 814,531 868,425 956,407 1026,333"
                  fill="none" stroke="#ffffff" stroke-width="1.6"/>
        <g fill="#ffffff">
          <circle cx="656" cy="532" r="3.5"/>
          <circle cx="692" cy="570" r="3.5"/>
          <circle cx="738" cy="497" r="3.5"/>
          <circle cx="814" cy="531" r="3.5"/>
          <circle cx="868" cy="425" r="3.5"/>
          <circle cx="956" cy="407" r="3.5"/>
        </g>
        <circle cx="1026" cy="333" r="9" fill="#ffffff"/>
        <circle cx="1026" cy="333" r="3.5" fill="var(--ink-dark)"/>
      </svg>

      <div class="figure-slot" role="img" aria-label="Illustration of a businessman holding a briefcase, reaching up toward the top point of the growth line"></div>

      <div class="front-author">DANIEL OSTRANDER</div>
    </section>

  </div>
</div>
</body>
</html>
```